Business Card Design Project

I help solve problems that people have with real estate, so I buy homes for cash that they no longer want, can't afford, inherited, etc. and fix and sell them or rent them or take over mortgage payments. See website: www.quickdeedhomestead.com

Industry/Entity Type

Real Estate

Contact Information for Business Card

Not exactly sure. Looking for a design that either is similar to the website www.quickdeedhomestead.com or that reflects what I do as described below. If it can look a little luxurious to show I can buy the houses for cash and I fix them and sell them, it's a bonus. I seem to like some of the higher end things like foil or black or something that makes it stand out.

Font styles to use
Serif

Requirements
Nice to have
• I seem to like black or clear. I like things to stand out and be different.

```html
<!DOCTYPE html>
<html lang="en">
<head>
<meta charset="utf-8">
<title>Homestead Renewal – Business Card</title>
<link rel="stylesheet" href="https://fonts.googleapis.com/css2?family=Lora:wght@400;700&display=swap">
<style>
  :root {
    --stage: #2b2b2d;
    --card-black: #0f0f0f;
    --card-white: #ffffff;
    --green: #6abf2e;
    --green-deep: #3f8f1c;
    --green-light: #9fdc5a;
    --ink: #1a1a1a;
    --rule: #b9d99c;
  }
  * { box-sizing: border-box; margin: 0; padding: 0; }
  html, body { width: 1200px; height: 880px; overflow: hidden; }
  body {
    background: var(--stage);
    font-family: "Lora", Georgia, serif;
    position: relative;
  }
  .card {
    position: absolute;
    left: 260px;
    width: 680px;
    height: 388px;
    border-radius: 22px;
    overflow: hidden;
    box-shadow: 0 14px 30px rgba(0,0,0,.45);
  }
  .card--front { top: 28px; background: var(--card-black); }
  .card--back  { top: 462px; background: var(--card-white); }

  .brand-name {
    font-family: "Lora", Georgia, serif;
    font-weight: 700;
    color: var(--green);
    text-transform: uppercase;
    letter-spacing: 1px;
    line-height: 1;
    display: flex;
    align-items: center;
    gap: 14px;
  }
  .brand-name__mark {
    width: 22px; height: 22px;
    background: var(--green);
    flex: none;
  }

  /* front */
  .card--front .brand-name {
    position: absolute;
    left: 0; right: 0; top: 138px;
    justify-content: center;
    font-size: 40px;
  }
  .front-band {
    position: absolute;
    left: 0; right: 0; bottom: 0;
    height: 78px;
    background: linear-gradient(180deg, var(--green-light), var(--green) 45%, var(--green-deep));
    border-top: 4px solid var(--card-black);
    box-shadow: 0 -3px 0 #e9e9e9;
    display: flex; align-items: center; justify-content: center;
  }
  .front-band__web {
    color: #fff;
    font-size: 20px;
    letter-spacing: 4px;
  }

  /* back */
  .card--back .brand-name {
    position: absolute;
    left: 44px; top: 128px;
    font-size: 32px;
  }
  .brand-name__stack { display: flex; flex-direction: column; gap: 6px; }
  .divider {
    position: absolute;
    left: 330px; top: 48px;
    width: 1px; height: 140px;
    background: var(--rule);
  }
  .contact {
    position: absolute;
    left: 352px; top: 42px;
    color: var(--ink);
    font-size: 16px;
    line-height: 1.3;
  }
  .contact__name {
    color: var(--green);
    font-weight: 700;
    font-size: 20px;
    text-transform: uppercase;
  }
  .contact__role { font-size: 14px; margin-bottom: 6px; }
  .contact__line { display: flex; align-items: center; gap: 8px; margin-top: 4px; }
  .contact__icon { width: 18px; height: 18px; flex: none; }
  .wave { position: absolute; left: 0; top: 0; width: 680px; height: 388px; }
  .wave__web { font-family: "Lora", Georgia, serif; font-size: 15px; fill: #111; }
</style>
</head>
<body>

<section class="card card--front" aria-label="Card front">
  <div class="brand-name"><span class="brand-name__mark"></span>Homestead Renewal</div>
  <div class="front-band"><span class="front-band__web">www.quickdeedhomestead.com</span></div>
</section>

<section class="card card--back" aria-label="Card back">
  <svg class="wave" viewBox="0 0 680 388" aria-hidden="true">
    <defs>
      <linearGradient id="waveGreen" x1="0" y1="0" x2="0" y2="1">
        <stop offset="0" stop-color="#a3df5c"/>
        <stop offset="0.5" stop-color="#6abf2e"/>
        <stop offset="1" stop-color="#3f8f1c"/>
      </linearGradient>
      <path id="webCurve" d="M400,340 C520,315 610,270 675,220"/>
    </defs>
    <path d="M0,350 C300,345 540,300 680,170 L680,388 L0,388 Z" fill="url(#waveGreen)"/>
    <path d="M0,338 C300,332 540,275 662,150 C540,288 300,344 0,344 Z" fill="#111"/>
    <path d="M0,346 C300,341 540,294 680,166" fill="none" stroke="#fff" stroke-width="3"/>
    <text class="wave__web"><textPath href="#webCurve" startOffset="8%">www.quickdeedhomestead.com</textPath></text>
  </svg>

  <div class="brand-name">
    <span class="brand-name__mark"></span>
    <span class="brand-name__stack"><span>Homestead</span><span>Renewal</span></span>
  </div>
  <div class="divider"></div>

  <div class="contact">
    <div class="contact__name">Jon Avery</div>
    <div class="contact__role">CEO</div>
    <div>PO Box 48 Linden Avenue</div>
    <div>Oak Park, Illinois</div>
    <div class="contact__line">
      <svg class="contact__icon" viewBox="0 0 20 20" aria-hidden="true">
        <circle cx="10" cy="10" r="9" fill="none" stroke="#6abf2e" stroke-width="2"/>
        <rect x="7" y="5" width="6" height="10" rx="1" fill="none" stroke="#6abf2e" stroke-width="1.5"/>
      </svg>555 555 5555</div>
    <div class="contact__line">
      <svg class="contact__icon" viewBox="0 0 20 20" aria-hidden="true">
        <circle cx="10" cy="10" r="9" fill="#6abf2e"/>
        <rect x="5" y="7" width="10" height="7" fill="#fff"/>
        <path d="M5,7 L10,11 L15,7" fill="none" stroke="#6abf2e" stroke-width="1.2"/>
      </svg>info@quickdeedmail.com</div>
  </div>
</section>

</body>
</html>
```